Flyer To Solicit Donations for a Good Cause

Hi. I am running the distance of a marathon race to solicit donations for a charitable cause. I need a well designed flyer to help me solicit support from friends and others. The copy for the flyer is attached. There is a significant amount of written text so it will need to be laid out in a way that is easy to read but also mixes well with some good images and design appeal. I am open to creative ideas. I have also attached my photo and a photo of me shaking hands with Mayor Velidis of Delphi and president of the Concordant Aegean Fellowship. Also there are some photos of the areas. These photos don't have to be used except for the one of me shaking hands with the Mayor and a caption underneath it. Otherwise, I am open to other stock photos or graphics. Feel free to contact me if you have questions. Thank you !

Update: ONE SIDED FLYER

Requirements
Must have
• Photo of the Mayor and Dale with the caption identifying us; All of the copy/text.

```html
<!DOCTYPE html>
<html lang="en">
<head>
<meta charset="utf-8">
<title>A Special Journey – Donation Flyer</title>
<link href="https://fonts.googleapis.com/css2?family=Cinzel:wght@400;600;700&family=Great+Vibes&family=Tinos:ital,wght@0,400;0,700;1,400&display=swap" rel="stylesheet">
<style>
  :root {
    --backdrop: #8f8f8f;
    --paper: #f7f6f1;
    --ink: #1d1b16;
    --gold: #8a7428;
    --gold-light: #c9b36a;
    --olive: #6b6232;
    --olive-dark: #2f2c17;
    --white: #ffffff;
  }
  * { box-sizing: border-box; margin: 0; padding: 0; }
  html, body { width: 1200px; height: 1200px; overflow: hidden; }
  body { background: var(--backdrop); font-family: "Tinos", "Times New Roman", serif; color: var(--ink); }

  .flyer {
    position: absolute; left: 197px; top: 30px;
    width: 805px; height: 1140px;
    background: var(--paper);
    overflow: hidden;
  }

  /* Hero */
  .hero { position: absolute; left: 0; top: 0; width: 805px; height: 479px; }
  .hero-photo {
    position: absolute; inset: 0;
    background:
      linear-gradient(90deg, rgba(20,18,12,.55) 0%, rgba(20,18,12,0) 45%),
      linear-gradient(180deg, #c8ccd0 0%, #e9eaea 30%, #8d8a78 52%, #4d4a38 72%, #2c2a20 100%);
  }
  .hero-title { position: absolute; right: 38px; top: 22px; text-align: right; }
  .title-script {
    font-family: "Great Vibes", cursive; font-size: 86px; line-height: 1;
    color: var(--ink); margin-right: 4px;
  }
  .title-main {
    font-family: "Cinzel", serif; font-weight: 400; font-size: 88px; line-height: .9;
    color: var(--gold); letter-spacing: 3px; margin-top: -4px;
  }
  .title-main .cap { font-size: 112px; }
  .title-sub {
    font-family: "Cinzel", serif; font-weight: 700; font-size: 19.5px; line-height: 1.2;
    color: var(--white); text-align: center; margin-top: 8px;
    text-shadow: 0 1px 3px rgba(0,0,0,.6);
  }
  .hero-intro {
    position: absolute; right: 36px; top: 352px; width: 470px;
    font-size: 22px; line-height: 26px; color: var(--white); text-align: right;
    text-shadow: 0 1px 3px rgba(0,0,0,.7);
  }

  .rule { position: absolute; left: 0; top: 479px; width: 805px; height: 4px; background: var(--gold); }

  /* Left photo column */
  .photo-column {
    position: absolute; left: 0; top: 483px; width: 226px; height: 602px;
    background: var(--olive);
  }
  .photo {
    position: absolute; left: 22px; width: 186px;
    border: 2px solid var(--gold-light);
  }
  .photo-portrait {
    top: 14px; height: 262px;
    background: linear-gradient(180deg, #b9a98a 0%, #8d8676 40%, #2b2d38 70%, #1f212b 100%);
  }
  .photo-handshake {
    top: 296px; height: 226px;
    background: linear-gradient(180deg, #9aa0a6 0%, #bfb8a6 35%, #34363f 60%, #2a2c33 85%, #6d6a60 100%);
  }
  .photo-caption {
    position: absolute; left: 22px; top: 528px; width: 186px;
    font-size: 12.5px; line-height: 15px; font-style: italic; color: var(--white); text-align: center;
  }

  /* Story column */
  .story {
    position: absolute; left: 239px; top: 494px; width: 266px;
    font-size: 16px; line-height: 18px;
  }
  .story p + p { margin-top: 10px; }
  .drop-cap {
    float: left; font-size: 48px; line-height: 38px; color: var(--gold);
    margin: 2px 3px 0 0;
  }
  .story-link { color: var(--gold); font-weight: 700; font-size: 14px; display: block; }
  .story-ask {
    margin-top: 24px; font-style: italic; font-size: 29px; line-height: 36px; color: var(--gold);
  }

  /* Steps column */
  .steps {
    position: absolute; left: 523px; top: 496px; width: 258px;
    font-size: 15.5px; line-height: 18px;
  }
  .steps h2 {
    font-size: 17px; line-height: 20px; font-weight: 700; color: var(--gold); margin-bottom: 12px;
  }
  .steps ol { list-style: none; }
  .steps li { margin-bottom: 12px; padding-left: 20px; text-indent: -20px; }
  .steps .email { color: var(--gold); font-weight: 700; }

  /* Footer band */
  .footer-band {
    position: absolute; left: 0; top: 1085px; width: 805px; height: 55px;
    background: linear-gradient(180deg, var(--olive) 0%, var(--olive-dark) 100%);
    border-top: 3px solid var(--gold);
    display: flex; align-items: center; justify-content: center;
    font-family: "Cinzel", serif; font-size: 21px; color: var(--gold-light); letter-spacing: .5px;
  }
</style>
</head>
<body>
  <article class="flyer">
    <header class="hero">
      <div class="hero-photo" role="img" aria-label="Photograph of ancient stone columns and ruins at Delphi with mountains behind"></div>
      <div class="hero-title">
        <div class="title-script">A Special</div>
        <h1 class="title-main"><span class="cap">J</span>OURNEY</h1>
        <div class="title-sub">For Your Specific Prayers &amp; For An<br>Important Ancient Cause</div>
      </div>
      <p class="hero-intro">On December 4, 2016 Dale Whitmore will make a special running journey of 26 miles through the ancient lands of Apollo and Athena at Delphi on Mt. Parnassus in Greece.</p>
    </header>

    <div class="rule"></div>

    <aside class="photo-column">
      <div class="photo photo-portrait" role="img" aria-label="Portrait photo of Dale in a dark blazer"></div>
      <div class="photo photo-handshake" role="img" aria-label="Photo of Dale shaking hands with Mayor Velidis of Delphi"></div>
      <p class="photo-caption">Dale with Mayor Velidis of Delphi, president of the Concordant Aegean Fellowship</p>
    </aside>

    <section class="story">
      <p><span class="drop-cap">D</span>ale will adorn his running outfit with special cloth strips that will contain written prayers and petitions of people who will sponsor his journey by making a charitable donation to the Concordant Aegean Fellowship, an organization that preserves the land and the Delphic culture.
        <span class="story-link">www.concordant-aegean-fellowship.org</span></p>
      <p>The concept is simple and very powerful: as Dale runs, your written prayer on a cloth strip will flow and emanate in the wind --- being blessed by the spirits of this ancient and magical land --- asking unto the wind that your prayer be answered. This type of prayer practice dates back to ancient times. The Tibetan culture commonly uses prayer flags with special mantras and symbols.</p>
      <p class="story-ask">Will you make a<br>prayer for yourself or<br>a loved and support a<br>good cause?</p>
    </section>

    <section class="steps">
      <h2>Here is how to get your<br>prayer started:</h2>
      <ol>
        <li>1) Decide what you want your prayer, petition or intention to be.</li>
        <li>2) Define your prayer, petition or intention by writing it down.</li>
        <li>3) Refine it is concise, clear &amp; specific. (18 words or less is ideal for each strip cloth).</li>
        <li>4) Contact Dale at <span class="email">dwhitmore@whitmorelane.com</span> and tell him how many prayer cloth strips you wish to obtain. Dale will then send you the cloth for you to write your prayer and send back to him or he will write out the prayer for you. Dale can also answer any questions you may have.</li>
        <li>5) A minimum donation of $25 for each prayer cloth is requested. Checks can be made to the “Dale Whitmore/Concordant Aegean Fellowship” and mail to Dale T. Whitmore, Whitmore Lane PLC, 1475 Harbor Row, Ste. 210 Easton, Maryland 21601 or though online payment instructions sent by email from Dale as requested.</li>
      </ol>
    </section>

    <footer class="footer-band">Your Prayer Can Make A Difference For You &amp; For A Good Cause!</footer>
  </article>
</body>
</html>
```